Bluecrest Ore Company needs a company newsletter template

We need a 2-page editable newsletter template, that we can update monthly with various information and pictures. We would like an area to include our values: Be Safe, Be Honest, Be Responsible, Be Respectful, Be Great. Ideally we would have 2-3 bulk text areas to highlight different things each month, with area we an update a picture from time to time and maybe some text areas where we can add a fun fact type thing. Some of the areas we will include are production milestones (if any), monthly tenure, monthly new hires, highlighting an employee that demonstrates our value, community engagement, upcoming holidays/events, press releases. The exact content will likely change month to month but these will be some of the frequent topics. We are a copper Mine in northern Yukon. I've attached our Brand Guidelines and logo files. Our website is ravelorex.com if you want to see the style and type of photos from our site

```html
<!DOCTYPE html>
<html lang="en">
<head>
<meta charset="utf-8">
<title>Bluecrest Ore Company – April 2022 Newsletter</title>
<link href="https://fonts.googleapis.com/css2?family=DM+Sans:wght@300;400;500;600;700&display=swap" rel="stylesheet">
<style>
:root{
  --backdrop:#dcdcdc;
  --paper:#ffffff;
  --copper:#7b3a2f;
  --gold:#f2b824;
  --ink:#1a1a1a;
  --night:#14202c;
  --slate:rgba(34,44,62,.88);
  --sky:#cfdbe6;
}
*{margin:0;padding:0;box-sizing:border-box}
html,body{width:1200px;height:1149px;overflow:hidden;background:var(--backdrop)}
body{font-family:"DM Sans",Arial,sans-serif;color:var(--ink)}
.stage{position:absolute;left:0;top:0;width:1960px;height:1876px;transform:scale(.6122);transform-origin:0 0}
.page{position:absolute;width:918px;height:1187px;background:var(--paper);box-shadow:4px 6px 10px rgba(0,0,0,.25);overflow:hidden}
.page--front{left:42px;top:81px}
.page--inside{left:990px;top:485px}
.abs{position:absolute}
.photo{position:absolute}
.photo--landscape{background:linear-gradient(180deg,#b9cde0 0%,#dfe6ec 45%,#7d8178 75%,#e9edf0 100%)}
.photo--crew{background:linear-gradient(180deg,#dfe8f0 0%,#c9d3dc 30%,#3a4250 55%,#28324a 80%,#e4e9ee 100%)}
.photo--site{background:linear-gradient(180deg,#6f8fb0 0%,#2f4a2a 25%,#5d5a48 55%,#9b8f7c 100%)}
.photo--miner{background:radial-gradient(circle at 55% 55%,#6b4a35 0%,#2c2a33 45%,#15161e 100%)}
.band{position:absolute}
.issue-date{left:60px;top:50px;font-size:54px;font-weight:300;color:#fff;letter-spacing:1px}
.issue-title{left:58px;top:108px;font-size:54px;font-weight:700;color:var(--gold)}
.brand{font-weight:700;text-align:center;text-transform:uppercase;line-height:1.1}
.brand--header{left:420px;top:120px;width:280px;font-size:32px;color:#fff}
.brand--footer{left:54px;top:1085px;width:164px;font-size:22px;color:var(--copper)}
.hero-line{left:54px;top:260px;width:320px;font-size:33px;font-weight:500;line-height:36px;color:#fff;text-transform:uppercase}
.kicker{font-size:23px;font-weight:600;color:var(--copper)}
.kicker--gold{color:var(--gold)}
.lead{font-size:19.5px;line-height:21.8px;text-transform:uppercase;font-weight:400}
.lead--copper{color:var(--copper)}
.lead--light{color:#fff}
.body{font-size:16px;line-height:18px}
.body p+p{margin-top:18px}
.body--light{color:#fff}
.note{font-size:16px;line-height:18px}
.footer-band{left:343px;top:1064px;width:575px;height:92px;background:var(--night);border-top-left-radius:40px;border-bottom-left-radius:40px}
.footer-text{left:461px;top:1074px;width:440px;color:#fff;font-size:18.5px;font-weight:500;line-height:22px;text-transform:uppercase}
.footer-url{left:461px;top:1128px;color:#fff;font-size:18.5px}
.rule{left:54px;top:489px;width:347px;height:1.5px;background:var(--gold)}
.logo-card{left:54px;top:1053px;width:164px;height:134px;background:#fff;border-top-right-radius:22px}
.overlay-box{left:432px;top:865px;width:398px;height:322px;background:var(--slate)}
</style>
</head>
<body>
<main class="stage">

  <section class="page page--front" aria-label="Newsletter front page">
    <div class="photo photo--landscape" role="img" aria-label="Snowy mine landscape" style="left:688px;top:30px;width:230px;height:202px"></div>
    <svg class="abs" style="left:0;top:0" width="918" height="232" aria-hidden="true">
      <polygon points="808,0 918,0 918,112" fill="var(--gold)"/>
      <polygon points="0,0 688,0 793,232 0,232" fill="var(--copper)"/>
      <path d="M64 197 Q170 170 288 196 Q170 180 64 197Z" fill="var(--gold)"/>
    </svg>
    <div class="abs issue-date">APRIL 2022</div>
    <div class="abs issue-title">Newsletter</div>
    <div class="abs brand brand--header">Bluecrest Ore<br>Company</div>

    <div class="photo photo--crew" role="img" aria-label="Mine crew in hard hats and hi-vis gear standing in snow" style="left:44px;top:232px;width:874px;height:259px;clip-path:polygon(0 0,100% 0,100% 0,874px 0,874px 20%,833px 100%,0 100%)"></div>
    <div class="abs hero-line">Mining is performed 100% underground using longhole stoping methods</div>

    <div class="abs kicker" style="left:54px;top:510px">ARTICLE 01</div>
    <div class="abs body" style="left:54px;top:556px;width:355px">
      <p>Lorem ipsum dolor sit amet, consectetuer adipiscing elit, sed diam nonummy nibh euismod tincidunt ut laoreet dolore magna aliquam erat volutpat. Ut wisi enim ad minim veniam, quis nostrud exerci tation ullamcorper suscipit lobortis nisl ut</p>
      <p>&nbsp;aliquip ex ea commodo consequat. Duis autem vel eum iriure dolor in hendrerit in vulputate velit esse molestie consequat, vel illum dolore eu feugiat nulla facilisis at vero eros et &nbsp;aliquip ex ea commodo consequat. Duis autem vel eum iriure dolor in hendrerit in vulputate velit esse molestie consequat, vel illum dolore eu feugiat nulla facilisis at vero eros et</p>
    </div>

    <div class="photo photo--site" role="img" aria-label="Aerial view of the mine site in a forested valley" style="left:459px;top:516px;width:406px;height:188px;clip-path:polygon(0 0,100% 0,318px 100%,0 100%)"></div>
    <div class="abs kicker" style="left:465px;top:723px">ARTICLE 01</div>
    <div class="abs lead lead--copper" style="left:463px;top:767px;width:360px">Lorem ipsum dolor sit amet, consectetuer adipiscing elit, sed diam nonummy nibh euismod tincidunt ut laoreet dolore magna aliquam erat volutpat. Ut wisi enim ad minim veniam, quis nostrud</div>
    <div class="abs note" style="left:463px;top:921px">Exerci tation ullamcorper suscipit lobortis nisl ut</div>
    <div class="abs body" style="left:463px;top:957px;width:345px">&nbsp;aliquip ex ea commodo consequat. Duis autem vel eum iriure dolor in hendrerit in vulputate velit esse molestie consequat, vel illum dolore eu feugiat nulla facilisis at vero eros et z</div>

    <div class="photo photo--miner" role="img" aria-label="Underground miner in headlamp helmet inspecting the tunnel wall" style="left:55px;top:857px;width:346px;height:330px"></div>
    <div class="band footer-band"></div>
    <div class="abs footer-text">Lorem ipsum dolor sit amet, consectetuer adipiscing elit, sed diam nonummy nibh</div>
    <div class="abs footer-url">www.ravelorex.com</div>
  </section>

  <section class="page page--inside" aria-label="Newsletter inside page">
    <svg class="abs" style="left:0;top:0" width="918" height="480" aria-hidden="true">
      <polygon points="0,0 630,0 420,384 380,385 0,474" fill="var(--copper)"/>
    </svg>
    <div class="photo photo--miner" role="img" aria-label="Underground miner with headlamp working at the rock face" style="left:405px;top:28px;width:513px;height:356px;clip-path:polygon(0 0,395px 0,100% 90px,100% 100%,0 100%)"></div>
    <div class="abs kicker kicker--gold" style="left:52px;top:52px">ARTICLE 01</div>
    <div class="abs lead lead--light" style="left:54px;top:102px;width:350px">Lorem ipsum dolor sit amet, consectetuer adipiscing elit, sed diam nonummy nibh euismod tincidunt ut laoreet dolore magna aliquam erat volutpat. Ut wisi enim ad minim veniam, quis nostrud</div>
    <div class="abs note" style="left:54px;top:256px;color:#fff">Exerci tation ullamcorper suscipit lobortis nisl ut</div>
    <div class="abs body body--light" style="left:54px;top:293px;width:345px">&nbsp;aliquip ex ea commodo consequat. Duis autem vel eum iriure dolor in hendrerit in vulputate velit esse molestie consequat, vel illum dolore eu feugiat nulla facilisis at vero eros et z</div>

    <div class="abs rule"></div>
    <div class="abs kicker" style="left:54px;top:509px">ARTICLE 01</div>
    <div class="abs body" style="left:54px;top:555px;width:355px">
      <p>Lorem ipsum dolor sit amet, consectetuer adipiscing elit, sed diam nonummy nibh euismod tincidunt ut laoreet dolore magna aliquam erat volutpat. Ut wisi enim ad minim veniam, quis nostrud exerci tation ullamcorper suscipit lobortis nisl ut</p>
      <p>&nbsp;aliquip ex ea commodo consequat. Duis autem vel eum iriure dolor in hendrerit in vulputate velit esse molestie consequat, vel illum dolore eu feugiat nulla facilisis at vero eros et &nbsp;aliquip ex ea commodo consequat. Duis autem vel eum iriure dolor in hendrerit in vulputate velit esse molestie consequat, vel illum dolore eu feugiat nulla facilisis at vero eros et</p>
    </div>

    <div class="abs kicker" style="left:459px;top:439px">ARTICLE 01</div>
    <div class="abs body" style="left:459px;top:484px;width:355px">
      <p>Lorem ipsum dolor sit amet, consectetuer adipiscing elit, sed diam nonummy nibh euismod tincidunt ut laoreet dolore magna aliquam erat volutpat. Ut wisi enim ad minim veniam, quis nostrud exerci tation ullamcorper suscipit lobortis nisl ut</p>
      <p>&nbsp;aliquip ex ea commodo consequat. Duis autem vel eum iriure dolor in hendrerit in vulputate velit esse molestie consequat, vel illum dolore eu feugiat nulla facilisis at vero eros et &nbsp;aliquip ex ea commodo consequat. Duis autem vel eum iriure dolor in hendrerit in vulputate velit esse molestie consequat, vel illum dolore eu feugiat nulla facilisis at vero eros et</p>
    </div>

    <div class="photo photo--crew" role="img" aria-label="Mine crew in hard hats and hi-vis coveralls in a snowy landscape" style="left:54px;top:850px;width:864px;height:337px;clip-path:polygon(0 0,706px 0,100% 115px,100% 100%,0 100%)"></div>
    <div class="band logo-card"></div>
    <div class="abs brand brand--footer">Bluecrest Ore<br>Company</div>
    <div class="band overlay-box"></div>
    <div class="abs kicker kicker--gold" style="left:459px;top:881px">ARTICLE 01</div>
    <div class="abs body body--light" style="left:459px;top:927px;width:355px">
      <p>Lorem ipsum dolor sit amet, consectetuer adipiscing elit, sed diam nonummy nibh euismod tincidunt ut laoreet dolore magna aliquam erat volutpat. Ut wisi enim ad minim veniam, quis nostrud exerci tation ullamcorper suscipit lobortis nisl ut</p>
      <p>&nbsp;aliquip ex ea commodo consequat. Duis autem vel eum iriure dolor in hendrerit in vulputate velit esse molestie consequat, vel illum dolore eu feugiat nulla facilisis at vero eros et &nbsp;aliquip ex ea commodo consequat. Duis autem vel eum iriure dolor in hendrerit</p>
    </div>
  </section>

</main>
</body>
</html>
```